Training Company Needs a Web Design

We are a Training company that needs a website design completed for us. "The Harbor Loft" The website will be a 'community space' specialising in 'Change and Transformation'. It will be a 'space' where individuals can come to find out 'latest news', upcoming events and courses, chat with others and find 'tools and templates'. They will need to login as a 'Member'.

The final design needs to be professional but have a 'fun and interactive' feel and appeal to our target audience who are predominantly corporate individuals.

Target Market(s)

Corporate Individuals - they may have a Change or Project background

Industry/Entity Type

Business Consultant

Number of Pages Required

3 page

Font styles to use
Sans Serif

Requirements
Must have
• Design for 'Home Page'
• A professional and corporate 'feel' but be fun and interactive.
Nice to have
• A 'sense' of how some of the other pages may be designed or laid out.

```html
<!DOCTYPE html>
<html lang="en">
<head>
<meta charset="utf-8">
<title>The Harbor Loft – Home</title>
<link href="https://fonts.googleapis.com/css2?family=Raleway:wght@400;500;600;700&display=swap" rel="stylesheet">
<style>
:root{
  --orange:#ef4f24;
  --blue:#0f9bd7;
  --ink:#222222;
  --text:#555555;
  --muted:#888888;
  --grey-bg:#f4f4f4;
  --footer:#222222;
  --white:#ffffff;
  --line:#dddddd;
}
*{box-sizing:border-box;margin:0;padding:0}
html,body{width:1200px;height:2429px;overflow:hidden}
body{font-family:"Raleway",sans-serif;color:var(--text);background:var(--white);position:relative}
a{color:inherit;text-decoration:none}

/* hero */
.hero{position:absolute;left:0;top:0;width:1200px;height:560px;overflow:hidden}
.hero-photo{position:absolute;inset:0;background:linear-gradient(135deg,#6b6f78 0%,#9aa0a8 35%,#c9ccd1 60%,#7c7f86 100%)}
.hero-shade{position:absolute;inset:0;background:rgba(20,24,32,.35)}
.hero-wave{position:absolute;left:0;bottom:0;width:1200px;height:80px}
.brand{position:absolute;left:100px;top:50px;display:flex;align-items:center;gap:12px;color:var(--white);font-weight:500;font-size:22px;line-height:1.05}
.brand-dot{width:14px;height:14px;border-radius:50%;background:var(--white)}
.account{position:absolute;top:23px;right:100px;display:flex;gap:20px}
.btn-small{font-size:12px;height:32px;padding:0 20px;display:flex;align-items:center;border-radius:3px;color:var(--white)}
.btn-register{background:var(--orange)}
.btn-login{border:1px solid rgba(255,255,255,.85);padding:0 28px}
.nav{position:absolute;top:72px;right:100px;display:flex;gap:8px;font-size:15px;color:var(--white)}
.nav a{padding:6px 12px;border-radius:4px}
.nav a.active{border:1px solid rgba(255,255,255,.9)}
.hero-title{position:absolute;left:0;width:1200px;top:268px;text-align:center;color:var(--white);font-size:26px;font-weight:500;line-height:31px}
.slider-dots{position:absolute;right:44px;top:228px;display:flex;flex-direction:column;gap:14px}
.slider-dots span{width:12px;height:12px;border:2px solid var(--white);border-radius:50%}
.slider-dots span.on{background:var(--orange);border-color:var(--orange)}

/* section headings */
.heading{display:flex;align-items:flex-start;gap:10px}
.heading-mark{width:14px;height:14px;border-radius:50%;border:3px solid var(--orange);margin-top:10px}
.heading small{display:block;font-size:18px;color:var(--ink);font-weight:500;line-height:20px}
.heading strong{display:block;font-size:22px;color:var(--blue);font-weight:500;line-height:28px}
.heading.center{justify-content:center}

.btn{display:inline-flex;align-items:center;justify-content:center;height:34px;padding:0 18px;font-size:14px;border-radius:2px;color:var(--white)}
.btn-orange{background:var(--orange)}
.btn-dark{background:#444}
.btn-blue{background:var(--blue)}
.btn-outline{border:1px solid #666;color:var(--ink);background:var(--white)}

/* welcome */
.welcome{position:absolute;top:630px;left:0;width:1200px;text-align:center}
.welcome p{width:1060px;margin:40px auto 0;font-size:13px;line-height:22px}
.welcome .actions{margin-top:26px;display:flex;justify-content:center;gap:30px}
.welcome .actions .btn{width:112px}

/* news and events */
.feed{position:absolute;top:918px;left:0;width:1200px;height:495px;background:var(--grey-bg)}
.news{position:absolute;left:100px;top:42px}
.news-cards{display:flex;gap:28px;margin-top:24px}
.news-card{width:278px;height:331px;background:var(--white);border:1px solid var(--line);padding:5px}
.news-photo{height:158px;background:linear-gradient(135deg,#a9b4bf,#e4e7ea 55%,#7d8794)}
.news-card h3{font-size:15px;color:var(--ink);font-weight:600;margin:20px 6px 10px}
.news-card p{font-size:12px;line-height:20px;margin:0 6px}
.news-card .btn{margin:12px 6px 0;height:34px;font-size:13px}
.events{position:absolute;left:740px;top:42px;width:360px}
.event{display:flex;gap:18px;margin-top:24px}
.event:first-of-type{margin-top:24px}
.event-photo{width:120px;height:93px;flex:none;background:linear-gradient(135deg,#7fa8c8,#dfe8ef 55%,#5b6c7f)}
.event h4{font-size:14px;color:var(--ink);font-weight:600;margin:4px 0 6px}
.event p{font-size:12px;line-height:20px}
.event-meta{display:flex;gap:20px;font-size:10px;margin-top:6px;color:var(--text)}
.event-meta span{display:flex;align-items:center;gap:5px}
.events .list{margin-top:0}

/* chat band */
.chat-band{position:absolute;top:1413px;left:0;width:1200px;height:125px;background:var(--blue);display:flex;align-items:center;justify-content:center;gap:28px;color:var(--white)}
.chat-band h2{font-size:24px;font-weight:500}
.chat-band .btn{border:2px solid var(--white);height:38px;padding:0 18px;font-size:16px;margin-left:20px}

/* tools */
.tools{position:absolute;top:1578px;left:0;width:1200px;text-align:center}
.tools .intro{width:900px;margin:22px auto 0;font-size:13px;line-height:22px;color:var(--muted)}
.tool-cards{position:absolute;top:150px;left:100px;display:flex;gap:57px}
.tool-card{width:296px;height:340px;background:var(--white);border:1px solid var(--line);box-shadow:0 14px 12px -10px rgba(0,0,0,.25);padding-top:32px}
.tool-icon{width:110px;height:110px;border-radius:50%;margin:0 auto;display:flex;align-items:center;justify-content:center}
.tool-icon.blue{background:var(--blue)}
.tool-icon.orange{background:var(--orange);box-shadow:0 0 0 4px var(--white),0 0 0 6px var(--orange)}
.tool-card h3{font-size:15px;color:var(--ink);font-weight:600;margin:30px 0 10px}
.tool-card p{font-size:12px;line-height:20px;padding:0 40px}
.tool-card .btn{margin-top:14px;height:36px;font-size:13px}

/* footer */
.footer{position:absolute;top:2116px;left:0;width:1200px;height:262px;background:var(--footer);color:#cfcfcf}
.footer-brand{position:absolute;left:100px;top:68px;display:flex;align-items:center;gap:12px;color:var(--white);font-size:22px;font-weight:500;line-height:1.05}
.footer-about{position:absolute;left:100px;top:148px;width:240px;font-size:12px;line-height:20px}
.footer h5{font-size:14px;font-weight:500;color:var(--white);margin-bottom:16px}
.quick{position:absolute;left:370px;top:50px}
.quick li{list-style:none;font-size:13px;line-height:24px}
.contact{position:absolute;left:553px;top:50px}
.contact li{list-style:none;display:flex;align-items:flex-start;gap:16px;font-size:13px;line-height:28px}
.contact li svg{margin-top:8px;flex:none}
.newsletter{position:absolute;left:848px;top:50px;width:252px}
.newsletter p{font-size:12px;line-height:20px}
.newsletter .field{margin-top:14px;height:36px;border:1px solid #777;padding:0 10px;display:flex;align-items:center;font-size:12px;color:var(--white)}
.newsletter .btn{margin-top:12px;width:252px;height:34px;font-size:12px}
.bottom-bar{position:absolute;top:2378px;left:0;width:1200px;height:51px;background:var(--orange);color:var(--white);display:flex;align-items:center;padding:0 100px;font-size:12px}
.socials{margin-left:auto;display:flex;gap:18px}
.socials span{width:30px;height:30px;border:2px solid var(--white);border-radius:50%}
</style>
</head>
<body>

<header class="hero">
  <div class="hero-photo" role="img" aria-label="Photo of colleagues smiling around a meeting table with notes and documents"></div>
  <div class="hero-shade"></div>
  <svg class="hero-wave" viewBox="0 0 1200 80" preserveAspectRatio="none"><path d="M0 0 Q600 120 1200 0 L1200 80 L0 80 Z" fill="#ffffff"/></svg>
  <a class="brand" href="#"><span class="brand-dot"></span><span>The Harbor Loft</span></a>
  <div class="account">
    <a class="btn-small btn-register" href="#">Register</a>
    <a class="btn-small btn-login" href="#">Login</a>
  </div>
  <nav class="nav">
    <a class="active" href="#">Home</a>
    <a href="#">Latest News</a>
    <a href="#">Upcoming Events</a>
    <a href="#">Chat</a>
    <a href="#">Contact Us</a>
  </nav>
  <h1 class="hero-title">A ‘community’ where an individual<br>can go to learn, connect,<br>collaborate and share</h1>
  <div class="slider-dots"><span></span><span></span><span class="on"></span><span></span><span></span></div>
</header>

<section class="welcome">
  <div class="heading center"><span class="heading-mark"></span><div style="text-align:left"><small>Welcome To</small><strong>The Harbor Loft</strong></div></div>
  <p>Nemo enim ipsam voluptatem quia voluptas sit aspernatur aut odit aut fugit, sed quia consequ untur magni dolores eos qui ratione voluptatem sequi nesci unt. Neque porro quisquam est, qui dolorem ipsum quia dolor sit amet, consectetur, adipisci velit, sed quia non numquam eius modi tempora incidunt ut labore et dolore magnam ed quia non numquam eius modi tempora incidunt ut labore et dolore magnam aliquam quaerat voluptatem. Ut enim ad minima veniam, quis nostrum exercitationem ullam corporis suscipit laboriosam, nisi ut aliquid ex ea commodi consequatur? Quis autem vel eum iure reprehenderit qui in ea voluptate velit esse quam nihil molestiae consequatur.</p>
  <div class="actions"><a class="btn btn-orange" href="#">Read More</a><a class="btn btn-dark" href="#">Contact Us</a></div>
</section>

<section class="feed">
  <div class="news">
    <div class="heading"><span class="heading-mark"></span><div><small>Find Out</small><strong>Latest News</strong></div></div>
    <div class="news-cards">
      <article class="news-card">
        <div class="news-photo" role="img" aria-label="Photo of a business team meeting around a table with laptops"></div>
        <h3>Neque porro quisquam dolorem</h3>
        <p>Nemo enim ipsam voluptatem quia volup tas sit aspernatur aut odit aut fugit, sed quia conse quuntur magni dolores eosqui</p>
        <a class="btn btn-outline" href="#">Read More</a>
      </article>
      <article class="news-card">
        <div class="news-photo" role="img" aria-label="Photo of a group of colleagues collaborating in an office"></div>
        <h3>Neque porro quisquam dolorem</h3>
        <p>Nemo enim ipsam voluptatem quia volup tas sit aspernatur aut odit aut fugit, sed quia conse quuntur magni dolores eosqui</p>
        <a class="btn btn-outline" href="#">Read More</a>
      </article>
    </div>
  </div>
  <div class="events">
    <div class="heading"><span class="heading-mark"></span><div><small>Find Out</small><strong>Upcoming Events</strong></div></div>
    <div class="event">
      <div class="event-photo" role="img" aria-label="Photo of business people standing in an office"></div>
      <div><h4>EMPLOYERS</h4><p>Nemo enim ipsam voluptatem quia tas sit aspernatur aut odit aut fugit</p>
      <div class="event-meta"><span><svg width="10" height="10" viewBox="0 0 10 10"><rect x="1" y="2" width="8" height="7" fill="none" stroke="#ef4f24"/><line x1="1" y1="4" x2="9" y2="4" stroke="#ef4f24"/></svg>Jan 28</span><span><svg width="10" height="10" viewBox="0 0 10 10"><path d="M1 2h8v5H4L2 9V7H1z" fill="#ef4f24"/></svg>0 Comments</span></div></div>
    </div>
    <div class="event">
      <div class="event-photo" role="img" aria-label="Photo of colleagues talking at a desk"></div>
      <div><h4>EMPLOYERS</h4><p>Nemo enim ipsam voluptatem quia tas sit aspernatur aut odit aut fugit</p>
      <div class="event-meta"><span><svg width="10" height="10" viewBox="0 0 10 10"><rect x="1" y="2" width="8" height="7" fill="none" stroke="#ef4f24"/><line x1="1" y1="4" x2="9" y2="4" stroke="#ef4f24"/></svg>Jan 28</span><span><svg width="10" height="10" viewBox="0 0 10 10"><path d="M1 2h8v5H4L2 9V7H1z" fill="#ef4f24"/></svg>0 Comments</span></div></div>
    </div>
    <div class="event">
      <div class="event-photo" role="img" aria-label="Photo of a small team reviewing work together"></div>
      <div><h4>EMPLOYERS</h4><p>Nemo enim ipsam voluptatem quia tas sit aspernatur aut odit aut fugit</p>
      <div class="event-meta"><span><svg width="10" height="10" viewBox="0 0 10 10"><rect x="1" y="2" width="8" height="7" fill="none" stroke="#ef4f24"/><line x1="1" y1="4" x2="9" y2="4" stroke="#ef4f24"/></svg>Jan 28</span><span><svg width="10" height="10" viewBox="0 0 10 10"><path d="M1 2h8v5H4L2 9V7H1z" fill="#ef4f24"/></svg>0 Comments</span></div></div>
    </div>
  </div>
</section>

<section class="chat-band">
  <svg width="50" height="42" viewBox="0 0 50 42"><ellipse cx="20" cy="17" rx="19" ry="15" fill="#ffffff"/><path d="M8 28 L4 38 L16 30 Z" fill="#ffffff"/><ellipse cx="34" cy="24" rx="14" ry="11" fill="#ffffff" stroke="#0f9bd7" stroke-width="2"/><circle cx="13" cy="17" r="2" fill="#0f9bd7"/><circle cx="20" cy="17" r="2" fill="#0f9bd7"/><circle cx="27" cy="17" r="2" fill="#0f9bd7"/></svg>
  <h2>Want to chat with others!</h2>
  <a class="btn" href="#">Chat Now</a>
</section>

<section class="tools">
  <div class="heading center"><span class="heading-mark"></span><div style="text-align:left"><small>Check Our</small><strong>Tools and Templates</strong></div></div>
  <p class="intro">A unique destination for everything that practitioners need to execute best practice change management, transformation and project methodologies. The Harbor Loft’s offering will be positioned as a place of learning.</p>
  <div class="tool-cards">
    <article class="tool-card">
      <div class="tool-icon blue"><svg width="40" height="40" viewBox="0 0 40 40" fill="none" stroke="#fff" stroke-width="2"><rect x="14" y="6" width="18" height="24" fill="#0f9bd7"/><rect x="10" y="10" width="18" height="24" fill="#0f9bd7"/><line x1="14" y1="17" x2="24" y2="17"/><line x1="14" y1="22" x2="24" y2="22"/><line x1="14" y1="27" x2="24" y2="27"/></svg></div>
      <h3>TOOLS AND TEMPLATES</h3>
      <p>Nemo enim ipsam voluptatem quia volup tas sit aspernatur aut odit aut fugit, sed quia conse quuntur magni dolores</p>
      <a class="btn btn-blue" href="#">Read More</a>
    </article>
    <article class="tool-card">
      <div class="tool-icon orange"><svg width="40" height="40" viewBox="0 0 40 40" fill="none" stroke="#fff" stroke-width="2.5"><rect x="6" y="8" width="28" height="19"/><line x1="20" y1="27" x2="20" y2="32"/><line x1="13" y1="33" x2="27" y2="33"/></svg></div>
      <h3>TOOLS AND TEMPLATES</h3>
      <p>Nemo enim ipsam voluptatem quia volup tas sit aspernatur aut odit aut fugit, sed quia conse quuntur magni dolores</p>
      <a class="btn btn-orange" href="#">Read More</a>
    </article>
    <article class="tool-card">
      <div class="tool-icon blue"><svg width="44" height="40" viewBox="0 0 44 40" fill="#fff"><circle cx="22" cy="13" r="5"/><path d="M13 30 a9 9 0 0 1 18 0 Z"/><circle cx="10" cy="17" r="4"/><path d="M3 30 a7 7 0 0 1 12 -5 L13 30 Z"/><circle cx="34" cy="17" r="4"/><path d="M41 30 a7 7 0 0 0 -12 -5 L31 30 Z"/></svg></div>
      <h3>TOOLS AND TEMPLATES</h3>
      <p>Nemo enim ipsam voluptatem quia volup tas sit aspernatur aut odit aut fugit, sed quia conse quuntur magni dolores</p>
      <a class="btn btn-blue" href="#">Read More</a>
    </article>
  </div>
</section>

<footer class="footer">
  <div class="footer-brand"><span class="brand-dot"></span><span>The Harbor Loft</span></div>
  <p class="footer-about">Nemo enim ipsam voluptatem quia voluptas sit aspernatur aut odit aut fugit, sed quia conse quuntur magni dolores</p>
  <div class="quick">
    <h5>QUICK LINKS</h5>
    <ul><li>&gt;&gt; Home</li><li>&gt;&gt; Find a Job</li><li>&gt;&gt; Find Talent</li><li>&gt;&gt; Our Services</li><li>&gt;&gt; About us</li><li>&gt;&gt; Contact us</li></ul>
  </div>
  <div class="contact">
    <h5>CONTACT US</h5>
    <ul>
      <li><svg width="10" height="13" viewBox="0 0 10 13"><path d="M5 0a5 5 0 0 1 5 5c0 3-5 8-5 8S0 8 0 5a5 5 0 0 1 5-5z" fill="#fff"/><circle cx="5" cy="5" r="2" fill="#222"/></svg><span>Delmar Quay Road,<br>Tucson, Arizona</span></li>
      <li><svg width="12" height="10" viewBox="0 0 12 10"><rect width="12" height="10" fill="#fff"/><path d="M0 0l6 5 6-5" stroke="#222" fill="none"/></svg><span>Email: info@harborloft.com</span></li>
      <li><svg width="12" height="12" viewBox="0 0 12 12"><rect width="12" height="12" rx="2" fill="#fff"/><path d="M3 3c0 3 3 6 6 6l1-2-2-1-1 1c-1 0-2-1-2-2l1-1-1-2z" fill="#222"/></svg><span>Phone: +1500 7310 48</span></li>
    </ul>
  </div>
  <div class="newsletter">
    <h5>NEWSLETTER</h5>
    <p>Lorem ipsum dolor sit amet, consectetur adipiscing elit dignissimos.</p>
    <div class="field">Email</div>
    <a class="btn btn-orange" href="#">SIGN UP NOW</a>
  </div>
</footer>
<div class="bottom-bar">
  <span>© 2016 The Harbor Loft. All Rights Reserved</span>
  <div class="socials"><span></span><span></span><span></span><span></span></div>
</div>

</body>
</html>
```